Redesign business cards

We have a new logo and I am not that happy with the layout of our existing card and looking for a change. Font is a bit small and the green can be hard to read. Logo may need a tidy up as the copy I have is not that hi-res too so require you to produce a hi-res version of the logo for us too. There will be three individual business cards to produce with just the names and phone numbers being different. Address will change too, but use what you see on the card for now.

Industry/Entity Type

Business

Requirements
Nice to have
• You could consider a redesign to the new logo, just not too radical. We like the blue and green hexagons as we feel that they are representative of oil industry that we are in.

```html
<!DOCTYPE html>
<html lang="en">
<head>
<meta charset="utf-8">
<title>Verdan Oil Services – Business Card</title>
<link rel="stylesheet" href="https://fonts.googleapis.com/css2?family=Alegreya:ital,wght@0,400;0,700;1,400&family=Arimo:wght@400;700&display=swap">
<style>
  :root {
    --paper: #ffffff;
    --ink: #2b2b2b;
    --muted: #5c5c5c;
    --band: #33383b;
    --band-text: #ffffff;
    --brand-green: #2e7d32;
    --brand-blue: #1f8fc8;
  }
  html, body {
    margin: 0;
    padding: 0;
    overflow: hidden;
    background: var(--paper);
  }
  .card {
    position: relative;
    width: 1200px;
    height: 741px;
    background: var(--paper);
    overflow: hidden;
  }
  .brand {
    position: absolute;
    left: 96px;
    top: 72px;
    display: flex;
    align-items: center;
    gap: 18px;
  }
  .brand .mark {
    width: 40px;
    height: 40px;
    background: var(--brand-blue);
  }
  .brand .wordmark {
    font-family: "Alegreya", Georgia, serif;
    font-weight: 700;
    font-size: 48px;
    line-height: 1;
    color: var(--brand-green);
  }
  .identity {
    position: absolute;
    left: 96px;
    top: 228px;
    padding-left: 32px;
    border-left: 6px solid var(--brand-green);
    font-family: "Alegreya", Georgia, serif;
  }
  .identity .name {
    margin: 0;
    font-size: 60px;
    font-weight: 700;
    line-height: 1.1;
    color: var(--ink);
  }
  .identity .credentials {
    font-size: 34px;
    font-weight: 400;
    color: var(--muted);
    margin-left: 10px;
  }
  .identity .role {
    margin: 10px 0 0;
    font-size: 36px;
    font-style: italic;
    color: var(--muted);
  }
  .identity .phone {
    margin: 8px 0 0;
    font-size: 38px;
    font-weight: 700;
    color: var(--ink);
    display: flex;
    align-items: center;
    gap: 14px;
  }
  .identity .phone svg { width: 30px; height: 30px; fill: var(--brand-green); }
  .contact-band {
    position: absolute;
    left: 0;
    bottom: 0;
    width: 1200px;
    height: 176px;
    background: var(--band);
    border-top: 8px solid var(--brand-green);
    box-sizing: border-box;
    padding: 34px 96px 0;
    font-family: "Arimo", Arial, sans-serif;
    font-style: normal;
    font-size: 30px;
    color: var(--band-text);
  }
  .contact-band .row {
    display: flex;
    gap: 80px;
    margin: 0 0 22px;
    white-space: nowrap;
  }
  .contact-band .item {
    display: flex;
    align-items: center;
    gap: 14px;
  }
  .contact-band svg {
    width: 28px;
    height: 28px;
    fill: none;
    stroke: var(--brand-blue);
    stroke-width: 2.2;
    flex: none;
  }
</style>
</head>
<body>
  <main class="card">
    <header class="brand">
      <span class="mark"></span>
      <span class="wordmark">Verdan Oil Services</span>
    </header>

    <section class="identity">
      <h1 class="name">Daniel Whitcombe<span class="credentials">NZCE (Mech) P&amp;P</span></h1>
      <p class="role">Director</p>
      <p class="phone">
        <svg viewBox="0 0 24 24" aria-hidden="true"><path d="M6.6 10.8a15.1 15.1 0 0 0 6.6 6.6l2.2-2.2a1 1 0 0 1 1-.25 11.4 11.4 0 0 0 3.6.57 1 1 0 0 1 1 1V20a1 1 0 0 1-1 1A17 17 0 0 1 3 4a1 1 0 0 1 1-1h3.5a1 1 0 0 1 1 1c0 1.25.2 2.45.57 3.57a1 1 0 0 1-.25 1z"/></svg>
        +614 555 01842
      </p>
    </section>

    <address class="contact-band">
      <div class="row">
        <span class="item">
          <svg viewBox="0 0 24 24" aria-hidden="true"><rect x="3" y="5" width="18" height="14" rx="1.5"/><path d="M3.5 6l8.5 7 8.5-7"/></svg>
          daniel@verdanoil.co.nz
        </span>
        <span class="item">
          <svg viewBox="0 0 24 24" aria-hidden="true"><circle cx="12" cy="12" r="9"/><path d="M3 12h18M12 3c3 3.2 3 14.8 0 18M12 3c-3 3.2-3 14.8 0 18"/></svg>
          www.verdanoil.com.au
        </span>
      </div>
      <div class="row">
        <span class="item">
          <svg viewBox="0 0 24 24" aria-hidden="true"><path d="M12 21s-7-6.2-7-11.5a7 7 0 0 1 14 0C19 14.8 12 21 12 21z"/><circle cx="12" cy="9.5" r="2.5"/></svg>
          Unit 214/560 Harlow st, Kelvin Grove, Queensland 4059
        </span>
      </div>
    </address>
  </main>
</body>
</html>
```